CareLumen business cards

We need a business card design that we could customize as needed for employees. We will need space for Name, Title, 1-2 phone numbers and email address.

We are a Pharmacy Benefits Management (PBM) company for hospice agencies and beginning a nationwide expansion. Attached is a vector file of our logo.

Cards can be single or double sided.

```html
<!DOCTYPE html>
<html lang="en">
<head>
<meta charset="utf-8">
<title>CareLumen business cards</title>
<link href="https://fonts.googleapis.com/css2?family=Didact+Gothic&family=Arimo:wght@700&display=swap" rel="stylesheet">
<style>
  :root {
    --canvas: #e9e7e3;
    --card-edge: #ffffff;
    --blue: #0f6a9c;
    --blue-deep: #0a5a8c;
    --cyan: #3fd4f0;
    --green: #8aa24a;
    --pale-green: #cfd8b6;
    --white: #ffffff;
  }
  * { box-sizing: border-box; margin: 0; padding: 0; }
  html, body { width: 1200px; height: 1000px; overflow: hidden; }
  body {
    background: var(--canvas);
    position: relative;
    font-family: "Didact Gothic", sans-serif;
  }
  .card {
    position: absolute;
    border: 3px solid var(--card-edge);
    overflow: hidden;
    box-shadow: 0 4px 14px rgba(0,0,0,.18);
  }
  /* Front */
  .card-front {
    left: 247px; top: 122px; width: 615px; height: 363px;
    border-radius: 62px 0 62px 0;
  }
  .front-art {
    position: absolute; inset: 0;
    background:
      radial-gradient(circle at 52% 62%, rgba(120,240,255,.75) 0%, rgba(63,212,240,.35) 18%, rgba(15,106,156,0) 45%),
      linear-gradient(160deg, #1a7fb8 0%, #1489c2 45%, #0e6fa8 100%);
  }
  .brand {
    position: absolute; display: flex; align-items: center; gap: 16px;
    color: var(--white); font-size: 50px; line-height: 1; letter-spacing: -0.5px;
  }
  .brand-front { left: 176px; top: 62px; }
  .brand-mark {
    width: 66px; height: 66px; background: var(--white); border-radius: 8px;
  }
  /* Back */
  .card-back {
    left: 250px; top: 505px; width: 653px; height: 380px;
    border-radius: 0 62px 0 62px;
    background: var(--white);
  }
  .quad { position: absolute; }
  .quad-tl { left: 0; top: 0; width: 317px; height: 193px; background: var(--green); }
  .quad-tr { left: 320px; top: 0; width: 333px; height: 190px; background: var(--blue); }
  .quad-bl { left: 0; top: 196px; width: 319px; height: 184px; background: var(--blue); }
  .quad-br { left: 322px; top: 193px; width: 331px; height: 187px; background: var(--green); }
  .back-square {
    position: absolute; left: 70px; top: 43px; width: 98px; height: 98px;
    border-radius: 10px; background: rgba(255,255,255,.35);
  }
  .center-block {
    position: absolute; left: 251px; top: 121px; width: 142px; height: 142px;
    background: var(--pale-green); border: 2px solid var(--white);
  }
  .brand-back { left: 346px; top: 56px; font-size: 43px; }
  .person {
    position: absolute; left: 54px; top: 268px;
    font-family: "Arimo", sans-serif; font-weight: 700;
    color: var(--white); font-size: 27px; line-height: 36px;
  }
  .contact {
    position: absolute; right: 30px; top: 259px;
    color: var(--white); font-size: 18px; line-height: 26px; text-align: right;
  }
  .contact li { list-style: none; display: flex; justify-content: flex-end; align-items: center; gap: 6px; }
  .contact svg { width: 17px; height: 17px; }
</style>
</head>
<body>
  <section class="card card-front" aria-label="Card front">
    <div class="front-art" role="img" aria-label="Glowing cyan light waves over a deep blue starry background"></div>
    <div class="brand brand-front"><span class="brand-mark"></span><span>CareLumen</span></div>
  </section>

  <section class="card card-back" aria-label="Card back">
    <div class="quad quad-tl"><span class="back-square"></span></div>
    <div class="quad quad-tr"></div>
    <div class="quad quad-bl"></div>
    <div class="quad quad-br"></div>
    <div class="center-block"></div>
    <div class="brand brand-back"><span>CareLumen</span></div>
    <p class="person">Name here<br>Title here</p>
    <ul class="contact">
      <li>12345678901
        <svg viewBox="0 0 20 20"><circle cx="10" cy="10" r="9" fill="#0f6a9c" stroke="#fff" stroke-width="1"/><path d="M7 5.5l2 2-1 1.3c.6 1.3 1.6 2.3 2.9 2.9l1.3-1 2 2-1.3 1.5c-3.3-.4-6.3-3.4-6.7-6.7z" fill="#fff"/></svg>
      </li>
      <li>12345678901
        <svg viewBox="0 0 20 20"><circle cx="10" cy="10" r="9" fill="#0f6a9c" stroke="#fff" stroke-width="1"/><rect x="7" y="5" width="6" height="10" rx="1" fill="none" stroke="#fff" stroke-width="1.3"/><circle cx="10" cy="13" r=".8" fill="#fff"/></svg>
      </li>
      <li>youremailaddress2here.com
        <svg viewBox="0 0 20 20"><circle cx="10" cy="10" r="9" fill="#0f6a9c" stroke="#fff" stroke-width="1"/><rect x="5.5" y="7" width="9" height="6.5" fill="#fff"/><path d="M5.5 7l4.5 3.6L14.5 7" fill="none" stroke="#0f6a9c" stroke-width="1"/></svg>
      </li>
    </ul>
  </section>
</body>
</html>
```